Awesome business card design needed

We need a new business card design to go with our new logo.
We are a web development agency that specialises in highly complex back-end integrations as opposed to design, our customers are retailers, hotels, hospitals and any other organisation that has a large online marketing department.
Take a look at our website - www.orvekplus.com for some inspiration.
We want our new business cards to exude class, professionalism and style.
We are likely to choose a high-end card to print them on but we want the design of the card itself to really turn heads.
We have no specific colour requirements, the logo as you will see is a turquoise colour R89 G171 B167 #59aba7 but it can also be in white if you want to make the colour of the card something different.
The information on the card should be:
Name
Position
Tel
email
Potentially a double sided card could have our web address, twitter and FB links.

```html
<!DOCTYPE html>
<html lang="en">
<head>
<meta charset="utf-8">
<title>Orvekplus Business Card</title>
<link rel="stylesheet" href="https://fonts.googleapis.com/css2?family=Cinzel:wght@400;600&display=swap">
<style>
  :root {
    --turquoise: #59aba7;
    --ink: #111214;
    --ink-soft: #2a2c30;
    --paper: #ffffff;
    --backdrop: #dcdcda;
    --text-dark: #1a1a1a;
    --text-light: #e8e8e8;
  }
  * { box-sizing: border-box; margin: 0; padding: 0; }
  html, body { width: 1200px; height: 900px; overflow: hidden; }
  body {
    background: var(--backdrop);
    font-family: "Cinzel", serif;
    position: relative;
  }
  .card {
    position: absolute;
    left: 280px;
    width: 640px;
    height: 366px;
    box-shadow: 0 8px 22px rgba(0,0,0,.22);
    overflow: hidden;
  }
  .texture {
    position: absolute;
    background: radial-gradient(ellipse at 50% 40%, var(--ink-soft), var(--ink) 75%);
  }

  /* Back face */
  .card-back { top: 50px; background: var(--ink); }
  .card-back .texture { inset: 0; }
  .card-back .wordmark {
    position: absolute; top: 118px; left: 0; right: 0;
    text-align: center;
    font-size: 64px; font-weight: 600; letter-spacing: 2px; line-height: 1;
    color: var(--turquoise);
  }
  .link-row {
    position: absolute; left: 30px; right: 30px; bottom: 40px;
    display: flex; justify-content: space-between; align-items: center;
    font-size: 11px; letter-spacing: .5px; color: var(--text-light);
    text-transform: uppercase;
  }
  .link-row .link { display: flex; align-items: center; gap: 6px; white-space: nowrap; }
  .link-row .marker {
    width: 11px; height: 11px; background: var(--turquoise); display: inline-block;
  }

  /* Front face */
  .card-front { top: 470px; background: var(--paper); }
  .card-front .top-band { top: 10px; left: 0; right: 0; height: 140px; }
  .card-front .wordmark {
    position: absolute; left: 32px; top: 84px;
    font-size: 56px; font-weight: 600; letter-spacing: 2px; line-height: 1;
    color: var(--turquoise);
  }
  .identity {
    position: absolute; right: 34px; top: 160px; text-align: right;
  }
  .identity .name {
    font-size: 24px; color: var(--turquoise); letter-spacing: 1.5px;
    border-bottom: 1px solid var(--turquoise); padding: 0 0 2px 40px;
  }
  .identity .role { font-size: 13px; color: var(--text-dark); letter-spacing: 1.5px; margin-top: 3px; }
  .rule {
    position: absolute; left: 30px; right: 30px; top: 230px;
    height: 1px; background: var(--turquoise);
  }
  .contacts { position: absolute; left: 34px; top: 248px; list-style: none; }
  .contacts li {
    display: flex; align-items: center; gap: 12px;
    font-size: 16px; letter-spacing: 2px; color: var(--text-dark);
    height: 26px;
  }
  .contacts .icon { width: 20px; height: 20px; }
  .card-front .bottom-band { left: 0; right: 0; top: 318px; height: 38px; }
  .quote {
    position: absolute; left: 0; right: 0; top: 329px;
    text-align: center; font-size: 12px; letter-spacing: 1px;
    color: var(--turquoise); white-space: nowrap;
  }
</style>
</head>
<body>

<section class="card card-back" aria-label="Card back">
  <div class="texture" role="img" aria-label="Dark perforated metal texture"></div>
  <div class="wordmark">orvekplus</div>
  <div class="link-row">
    <span class="link"><span class="marker"></span>www.orvekplus.com</span>
    <span class="link"><span class="marker"></span>linkhub.net/orvekplus</span>
    <span class="link"><span class="marker"></span>chatline.net/orvekplus</span>
  </div>
</section>

<section class="card card-front" aria-label="Card front">
  <div class="texture top-band" role="img" aria-label="Dark perforated metal texture"></div>
  <div class="wordmark">orvekplus</div>

  <div class="identity">
    <div class="name">Daniel Hartley</div>
    <div class="role">President</div>
  </div>

  <div class="rule"></div>

  <ul class="contacts">
    <li>
      <svg class="icon" viewBox="0 0 20 20" aria-hidden="true">
        <rect width="20" height="20" fill="#111214"/>
        <path d="M6 4 L8.5 4 L9.5 7 L8 8.2 Q9.5 11 11.8 12 L13 10.5 L16 11.5 L16 14 Q10 15 6 9 Q5 6 6 4 Z" fill="#59aba7"/>
      </svg>
      (000) 444 - 555 - 666
    </li>
    <li>
      <svg class="icon" viewBox="0 0 20 20" aria-hidden="true">
        <rect width="20" height="20" fill="#111214"/>
        <rect x="4" y="6" width="12" height="8" fill="none" stroke="#59aba7" stroke-width="1.3"/>
        <path d="M4 6 L10 11 L16 6" fill="none" stroke="#59aba7" stroke-width="1.3"/>
      </svg>
      info@orvekplus.com
    </li>
  </ul>

  <div class="texture bottom-band" role="img" aria-label="Dark perforated metal texture"></div>
  <p class="quote">"If you spend too much time thinking about a thing, you'll never get it done."</p>
</section>

</body>
</html>
```